Sign - Pricing "Menu" Board
Pimble Grove
Project: Sign - Pricing "Menu" Board
Sign - Pricing "Menu" Board  - Children
Creative Brief
This sign will be printed and be placed over desk for all customers to view. It will be in very large print in the front entrance for our new business so provide a quick pricing guide for our services. Our website can be viewed at https://pimblegrove.example.
Children
parents with kids under 7, day cares, pre-schools, grandparents, elementary schools
1. Cohesive feel with website 2. Include all of our services - Drop In Play, Pimble Sparks Programs, Memberships, Kids Night Out, Birthday Parties, Socks - $2 a pair Harriet & Gus Toys - prices vary 3. Our play place will feature home build by Tobby Nook homes. You can use photos from there site if you want. The playhouses can be found in their main street collection - we will feature (market, gas station, dr. office, animal hospital, diner) 4. We are looking for fun quick way for customers to see the pricing when they come in. 5. Everyone will need to sign a waiver to play. That should be included some place on the sign.

```html
<!DOCTYPE html>
<html lang="en">
<head>
<meta charset="utf-8">
<title>Pimble Grove – Pricing Board</title>
<link rel="stylesheet" href="https://fonts.googleapis.com/css2?family=Fredoka:wght@600;700&family=Patua+One&family=Nunito:wght@600;700;800&display=swap">
<style>
  :root{
    --blue:#1f5fbf;
    --blue-dark:#174a9c;
    --blue-stripe:#2a6bcc;
    --green:#6fb636;
    --green-dark:#4f9a1f;
    --green-light:#b4e07a;
    --text:#2a2a2a;
    --panel:#fbfdf6;
    --white:#ffffff;
  }
  *{box-sizing:border-box;margin:0;padding:0}
  html,body{width:1200px;height:595px;overflow:hidden;background:var(--white)}
  .board{position:relative;width:1200px;height:595px;overflow:hidden;font-family:"Nunito",sans-serif;color:var(--text);background:var(--white)}
  .board__backdrop{
    position:absolute;left:0;right:0;top:215px;bottom:0;
    background:repeating-linear-gradient(100deg,var(--blue) 0 22px,var(--blue-stripe) 22px 44px);
  }
  .board__photo{
    position:absolute;left:0;top:0;width:700px;height:235px;
    background:
      radial-gradient(ellipse 120px 110px at 110px 80px,#e9b98f 0%,#d9a27a 55%,rgba(217,162,122,0) 100%),
      radial-gradient(ellipse 160px 90px at 330px 150px,rgba(150,190,120,.55),rgba(150,190,120,0)),
      radial-gradient(ellipse 120px 80px at 250px 60px,rgba(230,120,110,.35),rgba(230,120,110,0)),
      linear-gradient(90deg,#cfd9c2 0%,#e6ebdf 45%,#f4f6f1 75%,#ffffff 100%);
  }
  .board__wave{position:absolute;left:0;top:150px;width:1200px;height:95px}
  .headline{position:absolute;left:640px;top:14px;width:540px;text-align:center}
  .headline__welcome{font-family:"Fredoka",sans-serif;font-weight:700;font-size:36px;color:var(--blue-dark);line-height:1}
  .headline__name{
    font-family:"Fredoka",sans-serif;font-weight:700;font-size:80px;line-height:1.05;
    color:var(--green);
  }
  .panel{position:absolute;background:var(--panel);border-radius:8px;box-shadow:0 3px 6px rgba(0,0,0,.25);padding:44px 14px 10px}
  .panel__title{
    position:absolute;left:0;right:0;top:0;height:34px;border-radius:8px 8px 0 0;
    background:linear-gradient(180deg,var(--green-light),#7cc242 55%,var(--green-dark));
    font-family:"Patua One",serif;font-weight:400;font-size:20px;color:var(--white);text-align:center;line-height:34px;
    text-shadow:0 1px 2px rgba(0,0,0,.35);
  }
  .panel__title--two{height:52px;line-height:23px;padding-top:3px}
  .list{list-style:none}
  .item{position:relative;padding-left:26px;margin-bottom:8px;font-size:14px;line-height:1.25;font-weight:700}
  .item__sub{display:block;font-weight:600}
  .tick{position:absolute;left:0;top:1px;width:18px;height:18px}
  .note{font-size:14px;font-weight:600;line-height:1.3}
  .note--indent{padding-left:26px}
  .note--gap{margin-top:10px}
  .note--italic{font-style:italic}
  .note strong{font-weight:800}
  .rule{border:0;border-top:1px solid #c9cfc0;margin:10px 0}
  .panel--weekdays{left:29px;top:240px;width:264px;height:156px}
  .panel--weekends{left:29px;top:413px;width:264px;height:163px}
  .panel--night{left:307px;top:240px;width:288px;height:336px;padding:48px 18px 10px}
  .panel--drop{left:614px;top:240px;width:255px;height:151px}
  .panel--members{left:614px;top:413px;width:255px;height:163px;padding-top:62px}
  .panel--sparks{left:888px;top:240px;width:283px;height:336px;padding-top:62px}
  .night__lead{font-size:16px;font-weight:800}
</style>
</head>
<body>
<main class="board">
  <div class="board__backdrop"></div>
  <div class="board__photo" role="img" aria-label="Photo of a smiling young child in a bright indoor play space"></div>
  <svg class="board__wave" viewBox="0 0 1200 95" preserveAspectRatio="none" aria-hidden="true">
    <path d="M0 40 C250 90 520 95 760 55 C950 25 1080 20 1200 35 L1200 70 C1080 58 950 62 760 85 C520 110 250 100 0 75 Z" fill="#7cc242"/>
    <path d="M0 40 C250 90 520 95 760 55 C950 25 1080 20 1200 35 L1200 45 C1080 32 950 38 760 66 C520 104 250 98 0 52 Z" fill="#b4e07a"/>
    <path d="M0 75 C250 100 520 110 760 85 C950 62 1080 58 1200 70 L1200 95 L0 95 Z" fill="#1f5fbf"/>
  </svg>

  <header class="headline">
    <div class="headline__welcome">Welcome to Our</div>
    <h1 class="headline__name">Pimble Grove.</h1>
  </header>

  <svg width="0" height="0" style="position:absolute">
    <symbol id="tick" viewBox="0 0 20 20"><path d="M2 11 L8 17 L18 3" fill="none" stroke="#4f9a1f" stroke-width="3.5" stroke-linecap="round" stroke-linejoin="round"/></symbol>
  </svg>

  <section class="panel panel--weekdays">
    <h2 class="panel__title">Weekdays</h2>
    <ul class="list">
      <li class="item"><svg class="tick"><use href="#tick"/></svg>Main Floor<span class="item__sub">Garden Party .....$150</span></li>
      <li class="item"><svg class="tick"><use href="#tick"/></svg>Mezzanine<span class="item__sub">Tree Top Party .....$175</span></li>
    </ul>
  </section>

  <section class="panel panel--weekends">
    <h2 class="panel__title">Weekends</h2>
    <ul class="list">
      <li class="item"><svg class="tick"><use href="#tick"/></svg>Main Floor<span class="item__sub">Garden Party .....$250</span></li>
      <li class="item"><svg class="tick"><use href="#tick"/></svg>Mezzanine<span class="item__sub">Tree Top Party .....$275<br>Busy Bee Package .....$650</span></li>
    </ul>
  </section>

  <section class="panel panel--night">
    <h2 class="panel__title">Kids Night Out</h2>
    <ul class="list">
      <li class="item night__lead"><svg class="tick"><use href="#tick"/></svg>Every Thursday Night<br>from 5pm – 8pm</li>
    </ul>
    <p class="note note--indent"><strong>$25</strong> per child<br><strong>$20</strong> each additional sibling</p>
    <p class="note note--indent note--gap">Must reserve spot,<br>limited availability</p>
    <hr class="rule">
    <ul class="list">
      <li class="item"><svg class="tick"><use href="#tick"/></svg>Everyone is required<br>to sign a waiver</li>
    </ul>
    <hr class="rule">
    <p class="note">Children must be supervised<br>at all times.</p>
  </section>

  <section class="panel panel--drop">
    <h2 class="panel__title">Drop In Play</h2>
    <ul class="list">
      <li class="item"><svg class="tick"><use href="#tick"/></svg>General Admission.....$12</li>
      <li class="item"><svg class="tick"><use href="#tick"/></svg>Each additional sibling.....$10</li>
    </ul>
  </section>

  <section class="panel panel--members">
    <h2 class="panel__title panel__title--two">Monthly<br>Memberships</h2>
    <ul class="list">
      <li class="item"><svg class="tick"><use href="#tick"/></svg>$45 Single</li>
      <li class="item"><svg class="tick"><use href="#tick"/></svg>$60 Family</li>
      <li class="item"><svg class="tick"><use href="#tick"/></svg>Socks are Required<span class="item__sub">$2.00 a pair</span></li>
    </ul>
  </section>

  <section class="panel panel--sparks">
    <h2 class="panel__title panel__title--two">Pimble Sparks<br>Programs</h2>
    <ul class="list">
      <li class="item"><svg class="tick"><use href="#tick"/></svg>Tuesday<span class="item__sub">Craft Activity .....$2.00</span></li>
      <li class="item"><svg class="tick"><use href="#tick"/></svg>Wednesday<span class="item__sub">STEM Activity .....$2.00</span></li>
      <li class="item"><svg class="tick"><use href="#tick"/></svg>Thursday<span class="item__sub">Interactive Reading<br>Activity .....$2.00</span></li>
      <li class="item"><svg class="tick"><use href="#tick"/></svg>Friday<span class="item__sub">Music Activity .....$2.00</span></li>
    </ul>
    <p class="note note--indent note--italic">(Plus cost of General<br>Admission)</p>
  </section>
</main>
</body>
</html>
```